CBD wholesaling/distribution website

I need a clean , professional looking website that is modern / but not cannabis themed. we are steering clear of anything green.

Coding

Coded - Design and coding required

Number of Pages Required

1 page

```html
<!DOCTYPE html>
<html lang="en">
<head>
<meta charset="utf-8">
<title>Veloran — CBD Wholesale &amp; Distribution</title>
<link rel="stylesheet" href="https://fonts.googleapis.com/css2?family=Raleway:wght@400;500;600;700;800&family=Open+Sans:ital,wght@0,400;1,400&family=Montserrat:wght@500;700&display=swap">
<style>
:root{
  --accent:#3566b8;
  --accent-deep:#1e3f78;
  --accent-band:#2c5aa6;
  --accent-light:#5f88cf;
  --accent-soft:#dfe8f7;
  --ink:#111;
  --text:#333;
  --white:#fff;
  --grey-line:#ddd;
  --brand-grey:#6a6a6a;
  --footer:#0d1626;
}
*{box-sizing:border-box;margin:0;padding:0}
html,body{width:1200px;height:3964px;overflow:hidden;background:var(--white)}
body{font-family:"Raleway",sans-serif;color:var(--text)}
.page{position:relative;width:1200px;height:3964px;overflow:hidden}
.abs{position:absolute}

/* header */
.site-header{position:absolute;left:0;top:0;width:1200px;height:88px;background:var(--white);z-index:3}
.logo{position:absolute;left:111px;top:22px;font-weight:800;font-size:37px;color:var(--accent);letter-spacing:.5px}
.call-pill{position:absolute;left:921px;top:11px;width:167px;height:29px;border-radius:15px;background:var(--accent);color:var(--white);font-weight:700;font-size:13px;line-height:29px;text-align:center}
.main-nav a{position:absolute;top:53px;font-weight:600;font-size:15px;color:var(--ink);text-decoration:none;letter-spacing:.2px}
.main-nav a.active::after{content:"";position:absolute;left:0;right:0;top:22px;height:4px;border-radius:2px;background:var(--accent)}

/* hero */
.hero{position:absolute;left:0;top:88px;width:1200px;height:792px;
  background:radial-gradient(ellipse 420px 360px at 860px 250px,#f2c86a 0%,#c98e34 26%,#5a4a4a 55%,transparent 80%),
  radial-gradient(ellipse 520px 500px at 1050px 620px,#3a5a96 0%,#1f3360 45%,transparent 80%),
  linear-gradient(90deg,#070d1a 0%,#0d1a33 45%,#1a2c52 75%,#24406f 100%)}
.hero-curve{position:absolute;left:0;top:680px}
.hero h1{position:absolute;left:111px;top:140px;font-size:50px;font-weight:800;color:var(--white);letter-spacing:1px}
.hero p{position:absolute;left:111px;top:235px;width:620px;font-size:20px;line-height:31px;color:var(--white);font-weight:500}
.btn-white{position:absolute;left:111px;top:343px;width:212px;height:55px;border-radius:28px;background:var(--white);color:var(--ink);font-weight:700;font-size:19px;line-height:55px;text-align:center}

.feature-card{position:absolute;top:569px;width:311px;height:311px;background:var(--white);box-shadow:0 4px 8px rgba(0,0,0,.15);text-align:center;z-index:2}
.feature-card.is-accent{background:var(--accent);color:var(--white)}
.feature-card h3{margin-top:50px;font-size:16px;font-weight:700;color:var(--ink)}
.feature-card.is-accent h3{color:var(--white)}
.feature-card .icon{display:block;margin:24px auto 0;width:83px;height:83px}
.feature-card p{margin:30px auto 0;width:237px;font-size:13px;line-height:17px;text-align:justify;text-align-last:center;color:var(--text)}
.feature-card.is-accent p{color:var(--white)}

/* section headings */
.section-title{position:absolute;font-weight:700;font-size:43px;color:var(--ink);letter-spacing:.5px}
.title-rule{position:absolute;height:5px;background:var(--accent-deep);border-radius:2px}

.btn-accent{position:absolute;height:43px;border-radius:22px;background:var(--accent);color:var(--white);font-weight:700;font-size:17px;line-height:43px;text-align:center}

/* about */
.about-text{position:absolute;left:114px;top:1050px;width:487px;font-size:13.5px;line-height:25.7px;text-align:justify;color:var(--text)}
.about-photo{position:absolute;left:717px;top:946px;width:372px;height:372px;border-radius:50%;
  background:radial-gradient(circle at 45% 55%,#e0a12c 0%,#b8781a 18%,#7a7a70 40%,#4c4c48 70%,#2e2e2c 100%)}

/* products */
.product{position:absolute;top:1643px;width:298px;text-align:center}
.product .photo{width:298px;height:298px;border-radius:50%;border-bottom:6px solid var(--accent)}
.product h3{margin-top:38px;font-size:25px;font-weight:600;color:var(--ink);letter-spacing:.3px}
.product p{margin-top:22px;font-size:13.5px;line-height:25.7px;text-align:justify;text-align-last:center;color:var(--text)}
.product .btn-accent{position:relative;display:block;margin:26px auto 0;width:148px}

/* testimonials */
.testimonials{position:absolute;left:0;top:2298px;width:1200px;height:642px;background:var(--accent);overflow:hidden}
.testimonials .band{position:absolute;left:0;top:0;width:1200px;height:18px;background:var(--accent-band)}
.testimonials h2{position:absolute;left:0;top:68px;width:1200px;text-align:center;font-weight:700;font-size:42px;color:var(--white)}
.testimonials .sub{position:absolute;left:0;top:130px;width:1200px;text-align:center;font-family:"Open Sans",sans-serif;font-size:20px;color:var(--accent-soft)}
.quote-mark{position:absolute;left:197px;top:183px}
.quote-text{position:absolute;left:250px;top:222px;width:760px;text-align:center;font-family:"Open Sans",sans-serif;font-style:italic;font-size:20px;line-height:34px;color:var(--white)}
.avatar{position:absolute;border-radius:50%;border:4px solid var(--white);background:linear-gradient(180deg,#c9d4dc 0%,#8da1b4 60%,#5a7390 100%)}
.client-rule{position:absolute;left:565px;top:512px;width:84px;height:2px;background:var(--accent-soft)}
.client-name{position:absolute;left:0;top:530px;width:1200px;text-align:center;font-weight:700;font-size:20px;color:var(--white)}
.dot{position:absolute;top:580px;width:13px;height:13px;border-radius:50%;border:2px solid var(--white)}
.dot.on{background:var(--accent-soft)}

/* brands */
.brand-grid{position:absolute;left:70px;top:3137px;width:1060px;height:339px}
.brand-grid .vline{position:absolute;top:0;width:1px;height:339px;background:var(--grey-line)}
.brand{position:absolute;width:240px;font-weight:700;font-size:24px;color:var(--brand-grey);display:flex;align-items:center;justify-content:center;gap:10px}
.brand .mark{width:18px;height:18px;border-radius:50%;background:var(--brand-grey);flex:none}

/* footer */
.site-footer{position:absolute;left:0;top:3645px;width:1200px;height:319px;background:var(--footer);text-align:center}
.footer-logo{position:absolute;left:0;top:36px;width:1200px;font-weight:800;font-size:52px;color:var(--accent-light)}
.footer-nav{position:absolute;left:0;top:118px;width:1200px;display:flex;justify-content:center;align-items:center;font-family:"Montserrat",sans-serif;font-weight:700;font-size:26px;color:var(--white)}
.footer-nav span{padding:0 22px}
.footer-nav i{display:block;width:3px;height:38px;background:var(--white);margin-top:-10px}
.copyright{position:absolute;left:0;top:172px;width:1200px;font-family:"Montserrat",sans-serif;font-weight:500;font-size:25px;color:var(--white)}
.social{position:absolute;top:253px;width:24px;height:24px;border-radius:5px;background:var(--white)}
</style>
</head>
<body>
<div class="page">

  <header class="site-header">
    <div class="logo">Veloran</div>
    <div class="call-pill">Call- 555 010 2040</div>
    <nav class="main-nav">
      <a class="active" style="left:523px">HOME</a>
      <a style="left:608px">ABOUT US</a>
      <a style="left:726px">SERVICES</a>
      <a style="left:838px">TESTIMONIALS</a>
      <a style="left:991px">CONTACT US</a>
    </nav>
  </header>

  <section class="hero" role="img" aria-label="Dark background with glowing amber smoke swirls">
    <svg class="hero-curve" width="1200" height="112" viewBox="0 0 1200 112" aria-hidden="true">
      <path d="M0 0 C60 20 110 45 130 112 L0 112 Z" fill="#fff"/>
    </svg>
    <h1>VELORAN</h1>
    <p>Lorem ipsum dolor sit amet, consectetur adipiscing elit, sed do eiusmod tempor incididunt ut labore et dolore magna</p>
    <div class="btn-white">READ MORE</div>
  </section>

  <div class="feature-card is-accent" style="left:115px">
    <h3>CONTACT US</h3>
    <svg class="icon" viewBox="0 0 83 83" aria-hidden="true">
      <circle cx="41.5" cy="41.5" r="39" fill="none" stroke="#fff" stroke-width="3"/>
      <path d="M30 24 h16 l8 8 v27 h-24 Z" fill="#fff"/>
      <path d="M37 37 c2 -1 3 0 3 2 l-1 2 c1 3 3 5 5 6 l2 -1 c2 0 3 1 2 3 c-1 2 -3 3 -5 2 c-5 -2 -8 -6 -9 -10 c0 -2 1 -3 3 -4 Z" fill="#3566b8"/>
    </svg>
    <p>Lorem ipsum dolor sit amet, consectetur adipiscing elit, sed do eiusmod tempor incididunt ut labore</p>
  </div>
  <div class="feature-card" style="left:441px">
    <h3>GET RECOMMENDATION</h3>
    <svg class="icon" viewBox="0 0 83 83" aria-hidden="true">
      <circle cx="41.5" cy="41.5" r="39" fill="none" stroke="#3566b8" stroke-width="3"/>
      <rect x="23" y="29" width="37" height="26" rx="3" fill="#3566b8"/>
      <path d="M24 31 L41.5 44 L59 31" fill="none" stroke="#fff" stroke-width="3"/>
    </svg>
    <p>Lorem ipsum dolor sit amet, consectetur adipiscing elit, sed do eiusmod tempor incididunt ut labore</p>
  </div>
  <div class="feature-card" style="left:767px">
    <h3>GO TO DISPENSERY</h3>
    <svg class="icon" viewBox="0 0 83 83" aria-hidden="true">
      <circle cx="41.5" cy="41.5" r="39" fill="none" stroke="#3566b8" stroke-width="3"/>
      <circle cx="41.5" cy="31" r="6" fill="#3566b8"/>
      <circle cx="29" cy="35" r="5" fill="#3566b8"/>
      <circle cx="54" cy="35" r="5" fill="#3566b8"/>
      <path d="M31 54 c0 -9 5 -14 10.5 -14 s10.5 5 10.5 14 Z" fill="#3566b8"/>
      <path d="M20 52 c0 -7 4 -11 9 -11 c2 0 3 1 4 2 c-2 3 -3 6 -3 9 Z" fill="#3566b8"/>
      <path d="M63 52 c0 -7 -4 -11 -9 -11 c-2 0 -3 1 -4 2 c2 3 3 6 3 9 Z" fill="#3566b8"/>
    </svg>
    <p>Lorem ipsum dolor sit amet, consectetur adipiscing elit, sed do eiusmod tempor incididunt ut labore</p>
  </div>

  <h2 class="section-title" style="left:109px;top:944px">ABOUT US</h2>
  <div class="title-rule" style="left:111px;top:1001px;width:214px"></div>
  <p class="about-text">Lorem ipsum dolor sit amet, consectetur adipiscing elit, sed do eiusmod tempor incididunt ut labore et dolore magna aliqua. Quis ipsum suspendisse ultrices gravida. Risus commodo viverra maecenas accumsan lacus vel facilisis. Lorem ipsum dolor sit amet, consectetur adipiscing elit, sed do eiusmod tempor incididunt ut labore et dolore magna aliqua. Quis ipsum suspendisse ultrices gravida. Risus commodo viverra maecenas accumsan lacus vel facilisis.</p>
  <div class="btn-accent" style="left:112px;top:1264px;width:148px">READ MORE</div>
  <div class="about-photo" role="img" aria-label="Hand holding an amber oil dropper bottle on a dark table"></div>

  <svg class="abs" style="left:0;top:1405px" width="1200" height="230" viewBox="0 0 1200 230" aria-hidden="true">
    <path d="M226 8 C600 -10 1000 60 1200 170 L1200 225 C1050 100 700 20 226 8 Z" fill="#3566b8"/>
  </svg>

  <h2 class="section-title" style="left:0;top:1520px;width:1200px;text-align:center">WHAT WE DO</h2>
  <div class="title-rule" style="left:474px;top:1579px;width:264px"></div>

  <div class="product" style="left:111px">
    <div class="photo" role="img" aria-label="Cartridge filled with golden oil on a soft background" style="background:radial-gradient(circle at 50% 50%,#e5b23a 0%,#d4aa5a 14%,#c9cfd8 38%,#9eabbf 70%,#6d7f9c 100%)"></div>
    <h3>PRODUCT NAME</h3>
    <p>Lorem ipsum dolor sit amet, consectetur adipiscing elit, sed do eiusmod tempor incididunt ut labore et dolore magna aliqua. Quis ipsum suspendisse ultrices</p>
    <div class="btn-accent">READ MORE</div>
  </div>
  <div class="product" style="left:437px">
    <div class="photo" role="img" aria-label="Heart shaped box filled with colourful gummy sweets" style="background:radial-gradient(circle at 60% 50%,#e07a3c 0%,#c96a4a 30%,#b77556 55%,#d9cfc8 85%,#cfc6bf 100%)"></div>
    <h3>PRODUCT NAME</h3>
    <p>Lorem ipsum dolor sit amet, consectetur adipiscing elit, sed do eiusmod tempor incididunt ut labore et dolore magna aliqua. Quis ipsum suspendisse ultrices</p>
    <div class="btn-accent">READ MORE</div>
  </div>
  <div class="product" style="left:763px">
    <div class="photo" role="img" aria-label="Glass dropper releasing a drop of oil into a bottle on a navy background" style="background:radial-gradient(circle at 50% 40%,#7a6a3a 0%,#4a5a8a 20%,#2f3f72 55%,#222f5a 100%)"></div>
    <h3>PRODUCT NAME</h3>
    <p>Lorem ipsum dolor sit amet, consectetur adipiscing elit, sed do eiusmod tempor incididunt ut labore et dolore magna aliqua. Quis ipsum suspendisse ultrices</p>
    <div class="btn-accent">READ MORE</div>
  </div>

  <section class="testimonials">
    <svg class="abs" style="left:0;top:0" width="1200" height="642" viewBox="0 0 1200 642" aria-hidden="true">
      <polygon points="0,251 1200,163 1200,642 0,642" fill="#5f88cf"/>
    </svg>
    <div class="band"></div>
    <h2>What our clients say ?</h2>
    <div class="sub">Our happy&nbsp; 1500⁺ clients feedback</div>
    <svg class="quote-mark" width="58" height="48" viewBox="0 0 58 48" aria-hidden="true">
      <path d="M2 46 V26 C2 12 9 3 22 1 L24 8 C16 10 13 15 13 22 H26 V46 Z M32 46 V26 C32 12 39 3 52 1 L54 8 C46 10 43 15 43 22 H56 V46 Z" fill="#fff"/>
    </svg>
    <p class="quote-text">Lorem ipsum dolor sit amet, consectetur adipiscing elit, sed do eiusmod tempor incididunt ut labore et dolore magna aliqua. Quis ipsum suspendisse ultrices</p>
    <div class="avatar" role="img" aria-label="Client portrait" style="left:310px;top:389px;width:70px;height:70px"></div>
    <div class="avatar" role="img" aria-label="Client portrait" style="left:418px;top:381px;width:86px;height:86px"></div>
    <div class="avatar" role="img" aria-label="Featured client portrait" style="left:539px;top:362px;width:124px;height:124px"></div>
    <div class="avatar" role="img" aria-label="Client portrait" style="left:698px;top:381px;width:86px;height:86px"></div>
    <div class="avatar" role="img" aria-label="Client portrait" style="left:826px;top:389px;width:70px;height:70px"></div>
    <div class="client-rule"></div>
    <div class="client-name">MAREK</div>
    <span class="dot" style="left:572px"></span>
    <span class="dot on" style="left:593px"></span>
    <span class="dot" style="left:614px"></span>
    <span class="dot" style="left:635px"></span>
  </section>

  <h2 class="section-title" style="left:0;top:3009px;width:1200px;text-align:center">OUR BRANDS</h2>
  <div class="title-rule" style="left:477px;top:3067px;width:250px"></div>
  <div class="brand-grid">
    <div class="vline" style="left:265px"></div>
    <div class="vline" style="left:528px"></div>
    <div class="vline" style="left:794px"></div>
    <div class="brand" style="left:11px;top:64px">Restora</div>
    <div class="brand" style="left:279px;top:64px">Summitline</div>
    <div class="brand" style="left:541px;top:64px"><span class="mark"></span>Nest Comfort</div>
    <div class="brand" style="left:807px;top:64px">Carovia</div>
    <div class="brand" style="left:11px;top:224px">Pulsewave</div>
    <div class="brand" style="left:279px;top:224px"><span class="mark"></span>Lateris Medical</div>
    <div class="brand" style="left:541px;top:224px">Corebase</div>
    <div class="brand" style="left:807px;top:224px">Halden Medical</div>
  </div>
  <div class="btn-accent" style="left:526px;top:3522px;width:148px">VIEW MORE</div>

  <footer class="site-footer">
    <div class="footer-logo">Veloran</div>
    <div class="footer-nav"><span>Home</span><i></i><span>About us</span><i></i><span>services</span><i></i><span>Blog</span><i></i><span>Contact us</span></div>
    <div class="copyright">@copyrightsVeloran 2019.All rights reserved</div>
    <span class="social" style="left:477px" aria-label="Social link"></span>
    <span class="social" style="left:532px" aria-label="Social link"></span>
    <span class="social" style="left:586px" aria-label="Social link"></span>
    <span class="social" style="left:640px" aria-label="Social link"></span>
    <span class="social" style="left:695px" aria-label="Social link"></span>
  </footer>

</div>
</body>
</html>
```